One of Australia's fastest growing energy maintenance contractors needs a new website

www.panelbrite.com.au
Our business has evolved over the past years and now our website is no longer relevant.
We clean solar panels and we vacuum roof gutters.
We clean solar panels on the roofs of residential houses right up to billion dollar solar farms with in excess of 1 million panels. We offer thermal image testing and bird proofing for our residential and commercial clients and thermal drone imaging services for our solar farm clients.
We vacuum clean roof gutters (using a LoftSuk) on the residential house next door right up to enormous private and public schools, colleges, shopping centres, strat complexes and commercial buildings.
When first built our business had more of a domestic residential skew and the website reflected that. While that is still part of our core business we are now bidding on and have secured large government, commercial and infrastructure contracts and our new website needs to reflect our growth and our new business. We need a new site that it optimised for both desktop ad phone viewing as our latest figures showed that 73% of people visiting our site are on mobile phones. We have an extensive amount of data on Trekmetrics available as well as Bidlinks. Both that would also need integrating with the site along with a few other plugins such as Kembo Chat IQ, Friendwall etc along with SEO key words etc. We are also the winner and finalists over multiple years of the small business of the year awards and we like to proudly and prominently display those on our site.
We are looking for a new site with a modern professional feel / theme
There is a definitive break in our business between the solar Panel cleaning clients and the gutter cleaning clients so we would like a home page that begins with a simple choice:
Solar Panel Cleaning – Gutter Cleaning
With a professional full screen background image (we have hundreds to choose from) and along the bottom a small area with rights reserved etc, phone number etc (at some point in the future we will split these into two businesses but for now it’s what we have).
After that selection is made we would like a repeat of that same scenario but the selection is:
If it’s Solar Panel Cleaning
(new background image)
Government – Infrastructure – Commercial – Residential
If it’s Gutter Cleaning
(new background image)
Government – Strata – Commercial – Residential
After making those choices then onto the relevant pages with background images relevant to each sector and a them that suits (on the residential we would like to keep the link to our trekmetrics reviews) - We will provide copy / text for each relevant page.
Other than that, a menu inclusive of the above and:
Resellers Portal – we will provide a link to this from Kembo CRM)
Customer portal (we will supply a link to this from our booking system)
We also need a page for our Solar Resellers / Partners page but we will give them a link to this, it won’t be listed on the site.
Request a quote page (Again we will provide information from Kembo as this will be linked to the CRM)
Standard contact us page inclusive of phone numbers, address and fields supplied from CRM
Sydney – 02 7391 5084
Southern Highlands – 02 4863 1507
Goulburn – 02 4863 1507
Canberra – 02 6178 3045
Wollongong – 02 4239 7615
sales@panelbrite.com.au
Head Office - Ferndell NSW 2583
ABN: 48762093115
Responsive Design: Optimized for desktop and mobile (73% mobile visitors).
Fast Loading Speed: Optimized for performance.
Smooth Transition Animations: For service and category selection.
Sticky Contact Bar: Always accessible at the bottom of mobile screens for quick calls.
SEO Optimization: Focused on government tenders, large-scale commercial contracts, and infrastructure projects.
Integrations
Trekmetrics & Trekmetrics Bidlinks.
Kembo Chat IQ.
Friendwall Beacon.
SEO tools and keyword optimization.
Many many more images available if needed

```html
<!DOCTYPE html>
<html lang="en">
<head>
<meta charset="utf-8">
<title>PanelBrite – Solar Panel &amp; Gutter Cleaning</title>
<link href="https://fonts.googleapis.com/css2?family=Lexend:wght@400;500;600&family=Outfit:wght@400;500;600&family=Oswald:wght@600&display=swap" rel="stylesheet">
<style>
:root{
  --navy:#0f3f7f;
  --blue:#1b63b5;
  --blue-mid:#1f7fd0;
  --sky:#2aa3e6;
  --ink:#1e2a3a;
  --muted:#4a5566;
  --line:#d7dee8;
  --white:#ffffff;
  --gold:#c9a23a;
  --orange:#f07a1e;
}
*{box-sizing:border-box;margin:0;padding:0}
html,body{width:1200px;height:4979px;overflow:hidden}
body{font-family:"Outfit",sans-serif;color:var(--ink);background:var(--white);position:relative;font-size:13px}
.abs{position:absolute}
h1,h2,h3{font-family:"Lexend",sans-serif;font-weight:500;color:var(--blue)}
.btn{display:inline-block;background:var(--sky);color:var(--white);font-size:12px;padding:0 16px;height:34px;line-height:34px;text-decoration:none}
.btn.dark{background:var(--blue)}
.hex{clip-path:polygon(50% 0,100% 25%,100% 75%,50% 100%,0 75%,0 25%)}
.mark{display:flex;align-items:center;justify-content:center;gap:8px}
.mark i{display:block;width:28px;height:1.5px;background:var(--sky)}
.mark b{display:block;width:16px;height:16px;border-radius:50%;background:var(--blue)}
.mark.light b{background:var(--white)}
p{font-size:12.5px;line-height:23px;color:var(--muted)}

.topbar{top:0;left:141px;width:918px;height:35px;background:var(--blue);color:var(--white);display:flex;align-items:center;font-size:12px}
.topbar .left{display:flex;gap:20px;padding-left:16px}
.topbar .right{margin-left:auto;display:flex;gap:22px;align-items:center;height:100%}
.topbar .quote{background:var(--sky);height:100%;padding:0 14px;display:flex;align-items:center}
.ico{display:inline-block;vertical-align:-2px;margin-right:6px}

.nav{top:35px;left:141px;width:918px;height:102px;background:var(--white);z-index:2;display:flex;align-items:center}
.logo{margin-left:18px;font-weight:600;font-size:18px;color:var(--blue);display:flex;align-items:center;gap:8px}
.logo span.sq{width:14px;height:14px;background:var(--blue)}
.menu{margin-left:auto;display:flex;align-items:center;font-size:12.5px;color:var(--navy);margin-right:20px}
.menu a{color:var(--navy);text-decoration:none;padding:0 22px;border-left:1px solid var(--line)}
.menu a:first-child{border:0;color:var(--blue);text-decoration:underline}
.search{width:28px;height:28px;background:var(--blue);margin-left:8px;display:flex;align-items:center;justify-content:center}

.hero{top:77px;left:0;width:1200px;height:551px;background:linear-gradient(180deg,#cfe0f4 0%,#b5cff0 45%,#3d6fc4 80%,#2350a5 100%)}
.hero-title{top:237px;left:141px;font-family:"Oswald",sans-serif;font-weight:600;font-size:37px;line-height:46px;color:var(--navy);text-transform:uppercase}
.hero-btns{top:439px;left:141px;display:flex;gap:16px}

.features{top:695px;left:141px;width:918px;display:flex}
.feat{width:242px;display:flex;gap:10px}
.feat h4{font-family:"Lexend",sans-serif;font-weight:500;font-size:14px;color:var(--blue);margin-bottom:6px}
.feat p{font-size:11.5px;line-height:20px}

.services-bg{top:800px;left:120px;width:1080px;height:640px;background:linear-gradient(90deg,rgba(255,255,255,0) 0%,#f2f5f9 50%,#e4eaf1 100%)}
.sec-title{width:1200px;left:0;text-align:center}
.sec-title h2{font-size:36px;margin-top:8px}
.block h3{font-size:26px;margin-bottom:16px}
.gutter-bg{top:1400px;left:0;width:620px;height:520px;background:linear-gradient(90deg,#e6ebf1 0%,rgba(255,255,255,0) 100%)}

.exp{background:var(--blue-mid);color:var(--white);text-align:center;font-family:"Lexend",sans-serif;display:flex;flex-direction:column;justify-content:center}

.why{top:2384px;left:0;width:1200px;height:504px;background:linear-gradient(100deg,#1a5aa6 0%,#1c74c8 55%,#27a0e3 100%);color:var(--white)}
.cols{top:2598px;left:141px;width:918px;display:flex}
.col{width:229px;text-align:center}
.col h4{font-family:"Lexend",sans-serif;font-weight:500;font-size:15px;margin:14px 0 6px}
.col p{color:rgba(255,255,255,.9);font-size:12px;line-height:20px;width:190px;margin:0 auto}
.btn.white{background:var(--white);color:var(--navy);font-size:12px}

.award{top:3105px;width:125px;height:125px;border-radius:50%}

.avatar{width:40px;height:40px;border-radius:50%;background:#b9c6d6}
.card{top:3445px;left:228px;width:294px;height:328px;background:var(--white);box-shadow:0 4px 24px rgba(20,50,90,.15);padding:26px 28px}
.card p{font-size:12px;line-height:22px;color:var(--ink)}
.stars{color:#f5a623;letter-spacing:1px;font-size:13px}

.touch{top:3918px;left:0;width:1200px;height:472px;background:linear-gradient(100deg,#1b64b8 0%,#2193da 60%,#2aa3e6 100%)}
.field{background:var(--white);height:33px;font-size:11px;color:var(--muted);padding:8px 12px}

.foot h5{font-family:"Lexend",sans-serif;font-weight:500;font-size:14px;color:var(--navy);margin-bottom:14px}
.foot li{list-style:none;font-size:12px;line-height:23px;color:var(--ink)}
</style>
</head>
<body>

<div class="abs topbar">
  <div class="left">
    <span><svg class="ico" width="13" height="10" viewBox="0 0 13 10"><rect x=".5" y=".5" width="12" height="9" fill="none" stroke="#fff"/><path d="M.5 .5l6 5 6-5" fill="none" stroke="#fff"/></svg>sales@panelbrite.com.au</span>
    <span><svg class="ico" width="11" height="11" viewBox="0 0 24 24"><path fill="#fff" d="M6.6 10.8a15 15 0 006.6 6.6l2.2-2.2c.3-.3.7-.4 1-.2 1.1.4 2.3.6 3.6.6.6 0 1 .4 1 1V20c0 .6-.4 1-1 1A17 17 0 013 4c0-.6.4-1 1-1h3.5c.6 0 1 .4 1 1 0 1.3.2 2.5.6 3.6.1.3 0 .7-.2 1z"/></svg>+61 2 4863 1507</span>
  </div>
  <div class="right">
    <span>Resellers Portal</span>
    <span>Customer Portal</span>
    <span class="quote">Request A Quote</span>
  </div>
</div>

<div class="abs nav">
  <div class="logo"><span class="sq"></span>PanelBrite</div>
  <nav class="menu">
    <a>Home</a><a>Solar Cleaning</a><a>Gutter Cleaning</a><a>About Us</a><a>Contact Us</a>
  </nav>
  <div class="search" style="margin-right:28px"><svg width="13" height="13" viewBox="0 0 14 14"><circle cx="6" cy="6" r="4.5" fill="none" stroke="#fff" stroke-width="1.8"/><path d="M9.5 9.5L13 13" stroke="#fff" stroke-width="1.8"/></svg></div>
</div>

<div class="abs hero" role="img" aria-label="Photo of a technician in a hard hat cleaning rooftop solar panels with a long-handled brush under a blue sky"></div>
<div class="abs hero-title">Professional Solar Panel<br>Cleaning &amp; Roof Gutter<br>Maintenance Keep Your System<br>Efficient And Your Home Safe!</div>
<div class="abs hero-btns"><a class="btn">Read More</a><a class="btn dark">Request A Quote</a></div>

<div class="abs features">
  <div class="feat">
    <svg width="46" height="40" viewBox="0 0 46 40" fill="none" stroke="#1b63b5" stroke-width="1.5"><path d="M3 14L23 3l20 11z"/><path d="M6 14v20M14 14v20M23 14v20M32 14v20M40 14v20M2 36h42"/></svg>
    <div><h4>Government</h4><p>Lorem ipsum dolor sit ame<br>consectetuer adipiscing.</p></div>
  </div>
  <div class="feat">
    <svg width="46" height="40" viewBox="0 0 46 40" fill="none" stroke="#1b63b5" stroke-width="1.5"><path d="M8 38V16h10v22M18 38V4h12v34M30 38V20h9v18M4 38h40"/><path d="M21 10h6M21 16h6M21 22h6M21 28h6"/></svg>
    <div><h4>Infrastructure</h4><p>Lorem ipsum dolor sit am<br>consectetuer adipiscing.</p></div>
  </div>
  <div class="feat">
    <svg width="46" height="40" viewBox="0 0 46 40" fill="none" stroke="#1b63b5" stroke-width="1.5"><path d="M4 38V12h16v26M20 38V6h22v32M2 38h42"/><path d="M8 18h8M8 24h8M8 30h8M25 12h12M25 19h12M25 26h12"/></svg>
    <div><h4>Commercial</h4><p>Lorem ipsum dolor sit am,<br>consectetuer adipiscing.</p></div>
  </div>
  <div class="feat">
    <svg width="46" height="40" viewBox="0 0 46 40" fill="none" stroke="#1b63b5" stroke-width="1.5"><path d="M4 18L23 4l19 14M8 16v22h30V16M18 38V26h10v12M2 38h42"/></svg>
    <div><h4>Residential</h4><p>Lorem ipsum dolor sit am<br>consectetuer adipiscing.</p></div>
  </div>
</div>

<div class="abs services-bg" role="img" aria-label="Faded photo of a worker cleaning solar panels"></div>
<div class="abs sec-title" style="top:838px"><div class="mark"><i></i><b></b><i></i></div><h2>Our Services</h2></div>

<div class="abs hex" style="top:966px;left:195px;width:280px;height:386px;background:linear-gradient(140deg,#1d3f7a,#3b6fb8 50%,#1a2f5a)" role="img" aria-label="Photo of solar panels being cleaned with a water-fed brush"></div>
<div class="abs block" style="top:1032px;left:616px;width:450px">
  <h3>Solar Panel Cleaning</h3>
  <p>We have a detailed knowledge of the cleaning &amp; testing of Solar Panels Visual &amp; thermal check of your panels with report to you included in the price We use only the best Ionic and LoftSuk cleaning systems<br>Pure water, Reverse Osmosis and De-Ionisation, suitable for even the hardest water conditions.<br>All staff are fully equipped, police checked, WWCC, trained and insured.</p>
  <a class="btn dark" style="margin-top:22px">Read More</a>
</div>

<div class="abs gutter-bg" role="img" aria-label="Faded photo of a worker on a roof"></div>
<div class="abs block" style="top:1480px;left:141px;width:440px">
  <h3>Gutter Cleaning</h3>
  <p>Blocked gutters may appear insignificant, but ensuring their proper functioning brings numerous benefits to your home.<br>Gutters play a crucial role in managing the flow of rainwater away from your house during storms or heavy downpours. When they become blocked, water can accumulate in the wrong places and even seep back into your home, causing damage to both the interior and exterior.</p>
  <a class="btn dark" style="margin-top:24px">Read More</a>
</div>
<div class="abs hex" style="top:1420px;left:690px;width:336px;height:382px;background:linear-gradient(160deg,#8a5a3c,#5e6b7a 55%,#2d4f7a)" role="img" aria-label="Photo of a technician vacuuming gutters at a brick building"></div>

<div class="abs hex" style="top:1903px;left:141px;width:150px;height:172px;background:linear-gradient(150deg,#9bb1c6,#3d5f87)" role="img" aria-label="Photo of a worker fitting solar panels"></div>
<div class="abs hex" style="top:1920px;left:262px;width:250px;height:285px;background:linear-gradient(160deg,#c9d6e0,#6d8a6a 60%,#3e5a3a)" role="img" aria-label="Photo of a house with a ladder and worker in the garden"></div>
<div class="abs hex" style="top:2140px;left:195px;width:122px;height:140px;background:linear-gradient(160deg,#6b7d5a,#3a4636)" role="img" aria-label="Photo of a gutter vacuum hose"></div>
<div class="abs hex exp" style="top:2100px;left:458px;width:124px;height:142px"><div style="font-size:28px;font-weight:600;line-height:30px">15</div><div style="font-size:14px;line-height:16px">Years<br>Experience</div></div>
<div class="abs block" style="top:1915px;left:641px;width:420px">
  <div class="mark" style="justify-content:flex-start"><b></b><i></i></div>
  <h3 style="font-size:34px;margin:10px 0 14px">About PanelBrite</h3>
  <p>PanelBrite are Residential, commercial, Government Lorem ipsum dol or sit amet, consectetuer adipiscing elit, sed diam nonummy nibh euism od tincidunt ut laoreet dolore magna aliquam erat volutpat. Ut wisi enim ad minim veniam, quis nostrud exerci tation ullamcorper suscipit lobortis nisl ut aliquip ex ea commodo consequat.<br>Duis autem vel eum iriure dolor in hendrerit in vulputate velit esse molestie consequat, vel illum dolore eu feugiat nulla facilisis at vero eros et accumsan et iusto odio dignissim qui blandit praesent luptatum zzril delenit augue duis dolore te feugait nulla facilisi.</p>
  <a class="btn dark" style="margin-top:24px">Read More</a>
</div>

<div class="abs why" role="img" aria-label="Blue tinted photo of a worker cleaning solar panels"></div>
<div class="abs sec-title" style="top:2474px;color:#fff"><div class="mark light"><b></b></div><h2 style="color:#fff;font-size:36px;margin-top:6px">Why Choose Us?</h2></div>
<div class="abs cols" style="color:#fff">
  <div class="col"><svg width="50" height="46" viewBox="0 0 50 46" fill="none" stroke="#fff" stroke-width="1.5"><circle cx="18" cy="8" r="5"/><path d="M10 44V24a8 8 0 0116 0v20M14 44V32M22 44V32"/><circle cx="38" cy="26" r="7"/><circle cx="38" cy="26" r="2.5"/></svg><h4>Experienced</h4><p>Our professional and experienced staff is ready to work on your project.</p></div>
  <div class="col"><svg width="50" height="46" viewBox="0 0 50 46" fill="none" stroke="#fff" stroke-width="1.5"><circle cx="25" cy="23" r="17"/><path d="M16 23l6 6 12-12"/></svg><h4>Jet Clean</h4><p>We work hard to ensure no damage happens to your property during our service.</p></div>
  <div class="col"><svg width="50" height="46" viewBox="0 0 50 46" fill="none" stroke="#fff" stroke-width="1.5"><circle cx="25" cy="24" r="18"/><circle cx="25" cy="24" r="13"/><path d="M25 14v10l7 5M22 4h6"/></svg><h4>Service On-Time</h4><p>We believe in reliable, prompt service for every project.</p></div>
  <div class="col"><svg width="50" height="46" viewBox="0 0 50 46" fill="none" stroke="#fff" stroke-width="1.5"><circle cx="25" cy="14" r="10"/><path d="M20 14l4 4 7-7M6 28l8 8h22l8-8M14 36v8M36 36v8"/></svg><h4>Quality</h4><p>Our mission is to provide high quality service at an affordable rate.</p></div>
</div>
<div class="abs" style="top:2764px;left:0;width:1200px;text-align:center"><a class="btn white">Request A Quote</a></div>

<div class="abs sec-title" style="top:3006px"><div class="mark"><i></i><b></b><i></i></div><h2 style="font-size:36px">Recognized for Excellence</h2></div>
<div class="abs award" style="left:143px;background:#3b4250;border:5px solid #d6dbe2" role="img" aria-label="Industry finalist award badge"></div>
<div class="abs award" style="left:288px;background:var(--orange);border:5px solid #ffd2ad" role="img" aria-label="Service award badge"></div>
<div class="abs award" style="left:444px;background:#f7a62b;border:5px solid #fbd48a" role="img" aria-label="Gutter cleaning award badge"></div>
<div class="abs award" style="left:605px;background:#14284a;border:6px solid var(--gold)" role="img" aria-label="Business award winner badge 2024"></div>
<div class="abs award" style="left:765px;background:#14284a;border:6px solid var(--gold)" role="img" aria-label="Business award winner badge 2022"></div>
<div class="abs award" style="left:925px;background:#14284a;border:6px solid var(--gold)" role="img" aria-label="Business award winner badge 2023"></div>

<div class="abs" style="top:3340px;left:141px">
  <div class="mark" style="justify-content:flex-start"><b></b><i></i></div>
  <h2 style="font-size:36px;margin-top:8px">What Our Clients Say</h2>
</div>
<div class="abs avatar" style="top:3463px;left:143px;width:54px;height:54px;border:3px solid var(--blue-mid);background:#c8d2de" role="img" aria-label="Client portrait"></div>
<div class="abs avatar" style="top:3539px;left:150px" role="img" aria-label="Client portrait"></div>
<div class="abs avatar" style="top:3597px;left:150px" role="img" aria-label="Client portrait"></div>
<div class="abs avatar" style="top:3657px;left:150px" role="img" aria-label="Client portrait"></div>
<div class="abs avatar" style="top:3711px;left:150px" role="img" aria-label="Client portrait"></div>
<div class="abs card">
  <div style="display:flex;justify-content:space-between;align-items:center;margin-bottom:30px"><span style="font-weight:600;font-size:13px;color:var(--blue)">Trekmetrics</span><span class="stars">★★★★★</span></div>
  <p>PanelBrite came on time. I was really well informed of any delay. The report is great and the feedback on our gutters and solar panels is full of detail. The before and after photos complete a professional job. I will be having both my gutters and solar panels regularly cleaned moving...Read More</p>
  <p style="margin-top:18px;line-height:18px">Mara Delwin<br>16 January 2025</p>
</div>
<div class="abs hex" style="top:3718px;left:520px;width:84px;height:96px;background:var(--blue);color:#fff;text-align:center;display:flex;flex-direction:column;justify-content:center;font-size:9.5px"><span class="stars" style="font-size:10px">★★★★★</span><span>4.9 | 392 reviews</span></div>
<div class="abs" style="top:3371px;left:686px;width:386px;height:547px;background:linear-gradient(160deg,#1f7fd0,#2aa3e6 50%,#1b63b5)" role="img" aria-label="Hexagon backdrop with a technician in an orange hard hat and overalls pointing toward the reviews"></div>

<div class="abs touch"></div>
<div class="abs" style="top:3918px;left:0;width:580px;height:472px;background:linear-gradient(160deg,#3f5c3a 0%,#4b6f9a 45%,#2a4d85 100%)" role="img" aria-label="Photo of a worker in a yellow hard hat scrubbing solar panels"></div>
<div class="abs" style="top:4000px;left:554px;width:505px;text-align:center;color:#fff">
  <div class="mark light"><b></b></div>
  <h2 style="color:#fff;font-size:36px;margin-top:4px">Get in Touch</h2>
</div>
<div class="abs" style="top:4090px;left:554px;width:505px;display:grid;grid-template-columns:1fr 1fr;gap:15px 12px">
  <div class="field">First name*</div><div class="field">Last name*</div>
  <div class="field">Email*</div><div class="field">Phone*</div>
  <div class="field" style="grid-column:1/3;height:69px">Message</div>
</div>
<div class="abs" style="top:4270px;left:722px;width:146px;height:29px;background:var(--sky);color:#fff;font-size:13px;font-weight:500;text-align:center;line-height:29px">SUBMIT NOW</div>

<div class="abs" style="top:4507px;left:141px;width:918px;height:140px;border:1px solid var(--line);background:#eef1e8" role="img" aria-label="Street map showing the head office location"></div>
<div class="abs" style="top:4507px;left:141px;width:213px;height:140px;background:linear-gradient(135deg,#1b63b5,#2aa3e6);display:flex;align-items:center;justify-content:center;gap:8px;color:#fff;font-weight:600;font-size:24px"><span style="width:16px;height:16px;background:#fff"></span>PanelBrite</div>

<div class="abs foot" style="top:4710px;left:141px"><h5>Quick Links</h5><ul><li>Home</li><li>Solar Cleaning</li><li>Gutter Cleaning</li><li>About Us</li><li>Contact Us</li></ul></div>
<div class="abs foot" style="top:4710px;left:294px;width:220px">
  <h5>Contact Details</h5>
  <div style="display:flex;gap:10px;font-size:12px;line-height:20px;margin-bottom:12px"><svg width="16" height="20" viewBox="0 0 16 20"><path d="M8 0a7 7 0 00-7 7c0 5 7 13 7 13s7-8 7-13a7 7 0 00-7-7z" fill="#1b63b5"/><circle cx="8" cy="7" r="2.5" fill="#fff"/></svg><span>8/22 Wattle Bend Road,<br>Ferndell NSW 2583</span></div>
  <div style="display:flex;gap:10px;font-size:12px;margin-bottom:12px"><svg width="16" height="16" viewBox="0 0 24 24"><path fill="#1b63b5" d="M6.6 10.8a15 15 0 006.6 6.6l2.2-2.2c.3-.3.7-.4 1-.2 1.1.4 2.3.6 3.6.6.6 0 1 .4 1 1V20c0 .6-.4 1-1 1A17 17 0 013 4c0-.6.4-1 1-1h3.5c.6 0 1 .4 1 1 0 1.3.2 2.5.6 3.6.1.3 0 .7-.2 1z"/></svg>+61 2 4863 1507</div>
  <div style="display:flex;gap:10px;font-size:12px"><svg width="16" height="12" viewBox="0 0 16 12"><rect width="16" height="12" fill="#1b63b5"/><path d="M0 0l8 6 8-6" fill="none" stroke="#fff"/></svg>sales@panelbrite.com.au</div>
</div>
<div class="abs foot" style="top:4750px;left:522px"><ul><li>Sydney – 02 7391 5084</li><li>Southern Highlands – 02 4863 1507</li><li>Goulburn – 02 4863 1507</li><li>Canberra – 02 6178 3045</li><li>Wollongong – 02 4239 7615</li></ul></div>
<div class="abs foot" style="top:4710px;left:779px;width:280px">
  <h5>Newsletter Sign Up</h5>
  <p style="font-size:12px;line-height:22px;color:var(--ink)">Subscribe to our newsletter to get the latest update to your inbox</p>
  <div style="display:flex;margin-top:14px"><div style="width:226px;height:40px;border:1px solid var(--line);font-size:11px;padding:12px 10px;color:var(--muted)">Your email address*</div><div style="width:54px;height:48px;margin-top:-8px;background:var(--blue);display:flex;align-items:center;justify-content:center"><svg width="22" height="22" viewBox="0 0 24 24"><path d="M2 11L22 2l-9 20-2-8z" fill="#fff"/></svg></div></div>
</div>
<div class="abs" style="top:4921px;left:141px;width:918px;height:1px;background:var(--line)"></div>
<div class="abs" style="top:4944px;left:141px;font-size:11px;color:var(--muted)">© 2025 PanelBrite. All Rights Reserved.</div>
<div class="abs" style="top:4944px;left:553px;font-size:11px;color:var(--muted)">ABN: 48762093115</div>
<div class="abs" style="top:4940px;left:1035px;width:22px;height:22px;border-radius:50%;background:var(--blue)"></div>
<div class="abs" style="top:4872px;left:1020px;width:96px;height:40px;border:1px solid #9aa7b6;border-radius:50%;background:#fff;font-size:8px;line-height:10px;text-align:center;padding-top:9px;color:var(--ink)">We're Online!<br>How may I help you today?</div>
<div class="abs" style="top:4885px;left:1127px;width:44px;height:44px;border-radius:50%;background:var(--blue);display:flex;align-items:center;justify-content:center"><svg width="20" height="20" viewBox="0 0 24 24"><path fill="#fff" d="M6.6 10.8a15 15 0 006.6 6.6l2.2-2.2c.3-.3.7-.4 1-.2 1.1.4 2.3.6 3.6.6.6 0 1 .4 1 1V20c0 .6-.4 1-1 1A17 17 0 013 4c0-.6.4-1 1-1h3.5c.6 0 1 .4 1 1 0 1.3.2 2.5.6 3.6.1.3 0 .7-.2 1z"/></svg></div>

</body>
</html>
```